Half page (a5) ad for a company

I need a design for an ad for a company to be published in a conference catalogue. Please find enclosed the logo for a company. The company is providing health screening services. Ad should be subtle and minimalistic, i.e. logo in the centre and a phrase saying: "Be in charge of your own health" and the website vantolix.co.uk. Also please find enclosed guidlines for colours and fonts to be used.

```html
<!DOCTYPE html>
<html lang="en">
<head>
<meta charset="utf-8">
<title>Vantolix Private – A5 Ad</title>
<link href="https://fonts.googleapis.com/css2?family=Montserrat:wght@400;700&display=swap" rel="stylesheet">
<style>
  :root {
    --brand-red: #e31e26;
    --deep-red: #9e0b1e;
    --ink: #000000;
    --paper: #ffffff;
    --backdrop: #efefef;
  }
  * { margin: 0; padding: 0; box-sizing: border-box; }
  html, body {
    width: 1200px;
    height: 1200px;
    overflow: hidden;
    background: var(--backdrop);
  }
  .ad {
    position: absolute;
    left: 216px;
    top: 58px;
    width: 767px;
    height: 1083px;
    background: var(--ink);
    font-family: "Montserrat", sans-serif;
    overflow: hidden;
  }
  .ad__backdrop {
    position: absolute;
    inset: 0;
    width: 100%;
    height: 100%;
  }
  .brand {
    position: absolute;
    left: 0;
    right: 0;
    top: 0;
    text-align: center;
    color: var(--brand-red);
    font-weight: 400;
  }
  .brand__mark {
    position: absolute;
    left: 50%;
    top: 200px;
    width: 110px;
    height: 110px;
    margin-left: -55px;
    border-radius: 50%;
    background: var(--brand-red);
  }
  .brand__name {
    position: absolute;
    left: 0;
    right: 0;
    top: 432px;
    font-size: 78px;
    line-height: 1;
    letter-spacing: 0.5px;
  }
  .brand__tier {
    position: absolute;
    left: 0;
    right: 0;
    top: 530px;
    font-size: 38px;
    line-height: 1;
    letter-spacing: 2px;
  }
  .tagline {
    position: absolute;
    left: 0;
    right: 0;
    top: 868px;
    text-align: center;
    color: var(--paper);
    font-weight: 700;
    font-size: 37px;
    line-height: 1;
  }
  .website {
    position: absolute;
    left: 0;
    right: 0;
    top: 927px;
    text-align: center;
    color: var(--brand-red);
    font-weight: 400;
    font-size: 22px;
    line-height: 1;
  }
</style>
</head>
<body>
  <main class="ad">
    <svg class="ad__backdrop" viewBox="0 0 767 1083" aria-hidden="true">
      <defs>
        <linearGradient id="swoosh" x1="0" y1="0" x2="1" y2="0">
          <stop offset="0" stop-color="var(--deep-red)" style="stop-color:#9e0b1e"/>
          <stop offset="0.55" stop-color="#e31e26"/>
          <stop offset="1" stop-color="#e31e26"/>
        </linearGradient>
      </defs>
      <rect class="ad__base" width="767" height="1083" fill="#000"/>
      <path class="ad__swoosh" d="M0,545 Q383,1040 767,548 L767,0 L0,0 Z" fill="url(#swoosh)"/>
      <path class="ad__top" d="M0,545 Q383,955 767,545 L767,0 L0,0 Z" fill="#fff"/>
    </svg>

    <div class="brand">
      <span class="brand__mark"></span>
      <h1 class="brand__name">Vantolix</h1>
      <p class="brand__tier">Private</p>
    </div>

    <p class="tagline">Be in charge of your own health</p>
    <p class="website">vantolix.co.uk</p>
  </main>
</body>
</html>
```